small business website design

***Update: need the design to be coded into a wordpress or similar format***
Need a website for a small business with big plans. No online ordering etc but business description and contact details pages, a page showing products we use and page for customers or suppliers to register with us. Also want links to chirpnest. We have a logo existing but also open to any improvements on the design. We have an existing website we created and looks very DIY but you can get some info from it to help create your design for us.
Hi Everyone, we didn't make it clear at the beginning but we would like the final design to be in a coded format and ready to upload to a URL. I have to apologise and admit to my lack of knowledge of the design process.
Oil / gas and industrial plant managers.
Small Business

```html
<!DOCTYPE html>
<html lang="en">
<head>
<meta charset="utf-8">
<title>KGL – Keystone Gauge Labs</title>
<link href="https://fonts.googleapis.com/css2?family=Open+Sans:wght@300;400;600&family=PT+Sans:wght@400;700&display=swap" rel="stylesheet">
<style>
  :root{
    --brand-blue:#2ea0cf;
    --brand-deep:#1b78a8;
    --logo-blue:#1d79ad;
    --page-grey:#f7f7f7;
    --white:#ffffff;
    --ink:#333333;
    --heading:#4a4a4a;
    --card-border:#dddddd;
    --footer:#2d2d2d;
    --footer-bottom:#222222;
    --footer-text:#c8c8c8;
    --muted-mark:#9a9a9a;
  }
  *{box-sizing:border-box;margin:0;padding:0}
  html,body{width:1067px;height:1200px;overflow:hidden}
  body{position:relative;background:var(--white);font-family:"Open Sans",Arial,sans-serif;color:var(--ink)}
  .abs{position:absolute}

  .top-band{left:0;top:0;width:1067px;height:412px;background:var(--brand-blue)}
  .welcome-band{left:0;top:412px;width:1067px;height:281px;background:var(--page-grey)}
  .frame{left:0;top:0}

  .brand{left:114px;top:28px;display:flex;align-items:center;gap:10px}
  .brand-dot{width:44px;height:44px;border-radius:50%;background:var(--logo-blue)}
  .brand-name{font-family:"PT Sans",sans-serif;font-weight:700;font-size:46px;line-height:1;color:var(--logo-blue);letter-spacing:1px}

  .main-nav{top:50px;left:0;font-family:"PT Sans",sans-serif;font-weight:700;font-size:13px;color:var(--white);letter-spacing:.3px}
  .main-nav a{position:absolute;top:0;color:inherit;text-decoration:none;white-space:nowrap}

  .search{left:747px;top:41px;width:226px;height:32px;border:1px solid #6fc0e2;border-radius:8px;background:var(--brand-blue);box-shadow:inset 0 0 0 1px #1f8ec0}
  .search span{position:absolute;left:23px;top:8px;font-family:Arial,sans-serif;font-size:11px;color:#eaf6fb}
  .search svg{position:absolute;right:10px;top:5px}

  .hero{left:100px;top:113px;width:865px;height:332px;border-radius:8px;background:linear-gradient(180deg,#3a4f8a 0%,#8a99c0 18%,#dfe3e6 30%,#e9ecee 58%,#6b4a2e 64%,#5a3c24 76%,#8ba1b4 84%,#c9d2d8 100%)}

  .welcome{left:0;top:470px;width:1067px;text-align:center}
  .welcome h1{font-family:"PT Sans",sans-serif;font-weight:700;font-size:29px;color:var(--heading);letter-spacing:.3px}
  .welcome p{width:810px;margin:14px auto 0;font-size:11.5px;line-height:17.8px;color:#333}
  .welcome p + p{margin-top:18px}
  .btn{display:inline-block;margin-top:18px;width:116px;height:24px;line-height:24px;background:linear-gradient(#2c9bd0,#1b78a8);color:var(--white);font-family:"PT Sans",sans-serif;font-weight:700;font-size:13.5px;letter-spacing:.8px;text-decoration:none}

  .fold-shadow{left:90px;top:693px;width:880px;height:14px;background:radial-gradient(ellipse at top,rgba(0,0,0,.09),rgba(0,0,0,0) 70%)}

  .card{top:799px;width:278px;height:252px;border:1px solid var(--card-border);border-radius:5px;background:linear-gradient(#fbfbfb,#efefef);text-align:center}
  .card h2{position:absolute;left:0;right:0;top:116px;font-weight:400;font-size:21.5px;letter-spacing:1px;color:#333}
  .card p{position:absolute;left:12px;right:12px;top:155px;font-family:Arial,sans-serif;font-size:11.5px;line-height:17px;color:#333}
  .card-photo{top:747px;width:155px;height:155px;border-radius:50%;border:4px solid #2893c3;box-shadow:0 0 0 3px #fff,0 0 0 4px #d5d5d5}

  .site-footer{left:0;top:1090px;width:1067px;height:83px;background:var(--footer)}
  .social{position:absolute;top:26px;width:36px;height:36px;border-radius:50%}
  .footer-brand{left:476px;top:20px;display:flex;align-items:center;gap:8px}
  .footer-brand .brand-dot{width:34px;height:34px;background:var(--muted-mark)}
  .footer-brand .brand-name{font-size:40px;color:var(--muted-mark)}
  .badge-a{left:669px;top:22px;width:184px;height:46px;border:2px solid #e4e4e4;border-radius:3px}
  .badge-b{left:913px;top:20px;width:66px;height:50px;border-radius:4px;background:#5b5b5b}

  .legal{left:0;top:1173px;width:1067px;height:27px;background:var(--footer-bottom);text-align:center;font-family:Arial,sans-serif;font-size:11.5px;line-height:27px;color:var(--footer-text)}
</style>
</head>
<body>
  <div class="abs top-band"></div>
  <div class="abs welcome-band"></div>

  <svg class="abs frame" width="1067" height="470" aria-hidden="true">
    <defs><filter id="soft" x="-5%" y="-5%" width="110%" height="115%"><feDropShadow dx="0" dy="2" stdDeviation="2" flood-opacity=".15"/></filter></defs>
    <path filter="url(#soft)" fill="#fff" d="M93,32 Q93,13 112,13 L300,13 Q328,13 343,42 Q362,86 410,86 L952,86 Q974,86 974,108 L974,441 Q974,453 962,453 L105,453 Q93,453 93,441 Z"/>
  </svg>

  <header>
    <div class="abs brand"><span class="brand-dot"></span><span class="brand-name">KGL</span></div>
    <nav class="abs main-nav">
      <a href="#" style="left:398px">HOME</a>
      <a href="#" style="left:500px">ABOUT &nbsp;KGL</a>
      <a href="#" style="left:637px">CONTACT US</a>
    </nav>
    <div class="abs search">
      <span>---Search your Topic here---</span>
      <svg width="24" height="22" viewBox="0 0 24 22"><circle cx="9" cy="9" r="6.5" fill="none" stroke="#e8f4fa" stroke-width="2"/><line x1="14" y1="14" x2="21" y2="20" stroke="#e8f4fa" stroke-width="3" stroke-linecap="round"/></svg>
    </div>
  </header>

  <div class="abs hero" role="img" aria-label="Row of white storage tanks at a waterfront terminal reflected in calm water"></div>

  <section class="abs welcome">
    <h1>WELCOME TO &nbsp;KGL</h1>
    <p>Lorem Ipsum is simply dummy text of the printing and typesetting industry. Lorem Ipsum has been the industry's standard dummy text ever since the 1500s, when an unknown printer took a galley of type and scrambled it to make a type specimen book.Lorem Ipsum has been the industry's standard dummy text ever since the 1500s, when an unknown printer took a galley of type and scrambled it to make.</p>
    <p>Standard dummy text ever since the industry's standard dummy text ever since the 1500s, when an unknown printer1500s, when an unknown printer took a Ipsum has been the industry's standard dummy text ever since galley of type.</p>
    <a class="btn" href="#">READ MORE</a>
  </section>

  <div class="abs fold-shadow"></div>

  <section>
    <article class="abs card" style="left:87px"><h2>Latest Ipsum</h2><p>Lorem Ipsum is simply dummy text of the printing and typesetting industry. Lorem Ipsum has been the industry's standard dummy text ever since the</p></article>
    <article class="abs card" style="left:391px"><h2>Latest Ipsum</h2><p style="top:160px">Lorem Ipsum is simply dummy text of the print-ing and typesetting industry. Lorem Ipsum has been the industry's standard dummy text ever since the</p></article>
    <article class="abs card" style="left:696px"><h2>Latest Ipsum</h2><p style="top:160px">Lorem Ipsum is simply dummy text of the print-ing and typesetting industry. Lorem Ipsum has been the industry's standard dummy text ever since the</p></article>

    <div class="abs card-photo" style="left:143px;background:linear-gradient(#9fb6c9,#6f7b58 55%,#4a4f3c)" role="img" aria-label="Two site workers in high-visibility gear at an industrial plant"></div>
    <div class="abs card-photo" style="left:453px;background:linear-gradient(#2c3f6e,#c98d5a 45%,#e6e6e6 60%,#6b5a3c)" role="img" aria-label="White pressurised storage vessels at dusk"></div>
    <div class="abs card-photo" style="left:752px;background:linear-gradient(#cfd6de,#4f6a8e 50%,#e8ecef)" role="img" aria-label="Radar level gauge transmitter mounted on a tank"></div>
  </section>

  <footer>
    <div class="abs site-footer">
      <a class="social" href="#" aria-label="chirpnest" style="left:101px;background:#1f4b7a"></a>
      <a class="social" href="#" aria-label="Social feed" style="left:146px;background:#2aa3e0"></a>
      <a class="social" href="#" aria-label="News feed" style="left:193px;background:#f0931a"></a>
      <a class="social" href="#" aria-label="Email" style="left:238px;background:#bdbdbd"></a>
      <div class="abs footer-brand"><span class="brand-dot"></span><span class="brand-name">KGL</span></div>
      <div class="abs badge-a"></div>
      <div class="abs badge-b"></div>
    </div>
    <div class="abs legal">Copyright © 2014 Keystone Gauge Labs Solutions | Disclaimer</div>
  </footer>
</body>
</html>
```